skyROAMER Helicopter Tour WordPress Website Design

SkyROAMER (skyroamer-example.com) is a premium helicopter tour company offering scenic flights in two Florida cities: Tampa and Sarasota. We are seeking a full Wordpress website redesign that is modern, upbeat, inviting, and highly conversion‑focused. The new site should feel energetic and trustworthy, reflect the excitement of helicopter sightseeing, and maintain our recognizable SkyROAMER color palette—while updating the overall look to feel fresh, clean, and current.
The website must be SEO‑friendly, mobile‑optimized, and easy to navigate. It should highlight our 5‑star customer reviews, showcase our tours clearly, and integrate seamlessly with TripLantern for instant online booking. The design should support a premium aviation experience while remaining friendly and accessible to tourists, families, couples, and adventure seekers.

These elements are essential and must be included in the design:

Brand & UX:
- Modern, upbeat, inviting design
- SEO‑friendly structure and layout
- Easy navigation and clear user flow
- Light grey “SR” background logo watermark (as used on current site)
- Clean, aviation‑inspired typography and layout

Conversion Features:
- Instant booking above the fold (TripLantern integration)
- Live Pindle Ratings carousel
- Tour comparison table (duration, route, price, etc.)
- FAQ expandable section
- Gift Cards page (highlighted as a major offering)
- What to Expect timeline (Arrive → Check‑In → Safety Briefing → Flight → Photos)
- Weather transparency widget (clear messaging about weather‑dependent flights

Content Structure:
- Separate pages for Tampa, Sarasota, and Gender Reveal Flights
- Pilot/Team profiles with short bios
- Highlighted features:
- Doors‑Off option
- Sunset flights
- Romantic packages
- Champagne add‑ons

Colors:
Use the existing SkyROAMER palette as the foundation, but modernize it.
- Background: Clean with the light grey “SR” watermark integrated tastefully.
The overall color direction should feel bright, premium, energetic, and trustworthy

Target Market(s)

Tourists visiting Tampa or Sarasota, Families looking for memorable activities, Couples seeking romantic experiences (sunset flights, proposals, anniversaries), Adventure seekers and content creators, Locals celebrating birthdays, holidays, or special occasions, Gender reveal clients looking for a unique aerial reveal experience

Industry/Entity Type

Travel & Tourism / Aviation / Helicopter Tours / Experience‑based Activities

Requirements
Must have
• These elements are essential and must be included in the design: Brand & UX - Modern, upbeat, inviting design / SEO‑friendly structure and layout / Easy navigation and clear user flow / Light grey “SR” background logo watermark (as used on current site) / Clean, aviation‑inspired typography and layout
Nice to have
• Interactive route map showing flight paths / Subtle motion or parallax effects in hero sections / Animated icons or micro‑interactions / Social media integration (Photavia grid, ClipNest clips) / Sticky mobile booking bar / Video header or short aerial footage loop / Subtle aviation‑themed graphic elements (rotor blur, sky gradients, etc.
Should not have
• No dark, heavy, or overly moody themes / No outdated fonts or overly playful typography / No cluttered layouts or excessive text blocks / No stocky, generic tourism imagery / No slow‑loading animations or heavy effects that hurt SEO

```html
<!DOCTYPE html>
<html lang="en">
<head>
<meta charset="utf-8">
<title>SkyROAMER Helicopter Tours – Tampa &amp; Sarasota</title>
<link rel="stylesheet" href="https://fonts.googleapis.com/css2?family=Michroma&family=Poppins:wght@400;500;600;700&display=swap">
<style>
:root{
  --navy:#0b1d3c;
  --navy-deep:#081630;
  --navy-mid:#10284f;
  --blue:#1c73c8;
  --blue-bright:#2a8be0;
  --line:#2a4773;
  --white:#ffffff;
  --muted:#9fb2cf;
  --ink:#1b2638;
  --grey-text:#5b6576;
  --star:#f4c21b;
}
*{box-sizing:border-box;margin:0;padding:0}
html,body{width:1200px;height:4208px;overflow:hidden}
body{font-family:"Poppins",sans-serif;background:var(--navy);color:var(--white);position:relative}
.abs{position:absolute}
section{position:absolute;left:0;width:1200px;overflow:hidden}
.frame-lines::before,.frame-lines::after{content:"";position:absolute;top:0;bottom:0;width:1px;background:var(--line);opacity:.6}
.frame-lines::before{left:113px}.frame-lines::after{left:1078px}
.btn{position:absolute;display:flex;align-items:center;font-size:10px;font-weight:600;letter-spacing:.06em;text-transform:uppercase;color:var(--white);background:var(--blue)}
.btn .label{flex:1;text-align:center;white-space:nowrap}
.btn .flag{width:30px;height:100%;display:flex;align-items:center;justify-content:center;border-left:1px solid rgba(255,255,255,.45)}
.section-title{position:absolute;left:0;width:1200px;text-align:center;font-family:"Michroma",sans-serif;font-weight:400;font-size:20px;letter-spacing:.01em;white-space:nowrap}
.watermark{position:absolute;font-family:"Poppins",sans-serif;font-weight:700;color:rgba(255,255,255,.035);font-size:120px;letter-spacing:.08em;white-space:nowrap}

/* header */
.site-header{position:absolute;top:0;left:0;width:1200px;height:100px;z-index:5}
.brand{position:absolute;left:119px;top:30px;display:flex;align-items:center;gap:8px;font-weight:600;font-size:15px;color:var(--white);letter-spacing:.03em}
.brand .dot{width:22px;height:22px;border-radius:50%;background:var(--blue-bright)}
.brand small{display:block;font-size:8px;letter-spacing:.2em;color:var(--blue-bright);text-align:right;font-weight:500}
.nav a{position:absolute;top:54px;font-size:9px;font-weight:600;letter-spacing:.08em;color:var(--white);text-decoration:none;white-space:nowrap}
.user-icon{position:absolute;left:814px;top:48px;width:20px;height:20px;border-radius:50%;border:1px solid rgba(255,255,255,.7)}
.weather{position:absolute;left:995px;top:44px;font-size:10px;line-height:1.15}
.weather b{font-size:14px;font-weight:500}

/* hero */
.hero{top:0;height:625px;background:linear-gradient(90deg,#0a1c3a 0%,#0f2a52 35%,#24466f 55%,#3a5a7c 75%,#16304f 100%)}
.hero-photo{position:absolute;left:470px;top:0;width:730px;height:625px;background:radial-gradient(ellipse at 55% 45%,#6d8aa6 0%,#34557a 45%,#15304f 80%)}
.hero-shade{position:absolute;left:0;top:0;width:760px;height:625px;background:linear-gradient(90deg,rgba(9,24,50,.96) 0%,rgba(12,33,66,.85) 55%,rgba(12,33,66,0) 100%)}
.hero h1{position:absolute;left:120px;top:218px;font-family:"Michroma",sans-serif;font-weight:400;font-size:26px;line-height:1.35;letter-spacing:.01em}
.hero p.lede{position:absolute;left:121px;top:302px;font-size:11px;color:#d6e1f0}
.badge{position:absolute;top:345px;height:40px;border:1px solid rgba(255,255,255,.45);border-radius:3px;display:flex;align-items:center;gap:7px;padding:0 10px;font-size:10px;background:rgba(10,28,58,.5);white-space:nowrap}
.badge .circ{width:16px;height:16px;border-radius:50%;background:var(--white);flex:none}
.badge small{display:block;font-size:6px;line-height:1.2}
.badge .stars{color:var(--star);font-size:8px;letter-spacing:1px}

/* booking */
.booking{position:absolute;left:122px;top:508px;width:956px;height:102px;background:var(--white);color:var(--ink);z-index:4}
.booking h2{position:absolute;left:16px;top:20px;font-family:"Michroma",sans-serif;font-size:12px;font-weight:400;white-space:nowrap}
.trip{position:absolute;top:23px;font-size:9px;display:flex;align-items:center;gap:5px;white-space:nowrap}
.trip i{display:inline-block;width:9px;height:9px;border-radius:50%;border:1px solid #777}
.trip i.on{background:var(--ink);border-color:var(--ink)}
.field{position:absolute;top:52px;height:33px;border:1px solid #c5ccd6;border-radius:2px;font-size:9px;color:#8a93a1;display:flex;align-items:center;padding:0 12px;justify-content:space-between;white-space:nowrap}

/* reviews */
.reviews{top:625px;height:401px;background:var(--navy)}
.review{position:absolute;top:90px;width:226px;height:248px;background:var(--navy-mid);border:1px solid var(--line);padding:26px 16px}
.review.faded{opacity:.35}
.review .who{display:flex;gap:10px;align-items:center}
.avatar{width:32px;height:32px;border-radius:50%;flex:none}
.review h3{font-family:"Michroma",sans-serif;font-size:10px;font-weight:400;line-height:1.25}
.review .when{font-size:8px;color:var(--muted)}
.review p{margin-top:22px;font-size:9.5px;line-height:1.75;color:#c8d4e6}
.review .stars{position:absolute;left:16px;bottom:16px;color:var(--star);font-size:14px;letter-spacing:3px}
.review .src{position:absolute;right:14px;bottom:18px;width:14px;height:14px;border-radius:50%;background:var(--white)}

/* featured */
.featured{top:1026px;height:579px;background:linear-gradient(180deg,#f7f8fa 0%,#efeae3 45%,#d9c6b0 80%,#cdb79f 100%);color:var(--ink)}
.featured .section-title{color:var(--ink)}
.feature{position:absolute;width:220px;text-align:center}
.feature .num{display:inline-block;font-size:11px;font-weight:600;margin-bottom:-6px;position:relative;z-index:2;background:#f6f4f1;padding:0 4px}
.feature .pic{width:122px;height:122px;border-radius:50%;margin:0 auto}
.feature h3{margin-top:22px;font-family:"Michroma",sans-serif;font-size:10.5px;font-weight:400;white-space:nowrap}
.feature p{margin:12px auto 0;width:200px;font-size:9.5px;line-height:1.55;color:var(--grey-text)}

/* gifts */
.gifts{top:1605px;height:404px;background:var(--navy)}
.gift{position:absolute;top:105px;width:230px;height:143px;border-radius:3px;display:flex;align-items:center;justify-content:center;font-size:17px;font-weight:500;font-style:normal;color:var(--white)}
.gift .corner{position:absolute;right:14px;top:12px;font-size:13px;font-weight:600}

/* pilots */
.pilots{top:2009px;height:462px;background:linear-gradient(90deg,#f4f7fb 0%,#e6edf5 35%,#c9d6e4 60%,#9fb1c3 100%);color:var(--ink)}
.pilots .photo{position:absolute;left:500px;top:0;width:700px;height:462px;background:radial-gradient(ellipse at 45% 45%,#6b5a4c 0%,#8a9bab 35%,#b7c5d3 70%,rgba(201,214,228,0) 100%)}
.pilots h2{position:absolute;left:121px;top:112px;font-family:"Michroma",sans-serif;font-size:19px;font-weight:400;white-space:nowrap}
.pilots p{position:absolute;left:121px;top:147px;width:330px;font-size:11px;line-height:1.72;color:#2b3646}

/* compare */
.compare{top:2471px;height:477px;background:var(--navy)}
.tour-table{position:absolute;left:320px;top:150px;width:758px;border-collapse:collapse;font-size:9.5px}
.tour-table th{background:var(--blue);height:28px;font-size:9px;font-weight:600;letter-spacing:.08em}
.tour-table td{height:30.5px;text-align:center;color:#c8d4e6;line-height:1.2}
.tour-table tr:nth-child(odd) td{background:#0e2547}
.tour-table tr:nth-child(even) td{background:#0b1f3d}

/* faq */
.faq{top:2948px;height:489px;background:linear-gradient(180deg,#f5f7fa 0%,#e6ecf2 40%,#a8b7c4 75%,#6f8494 100%);color:var(--ink)}
.faq .section-title{color:var(--ink)}
.faq-item{position:absolute;left:323px;width:554px;height:33px;background:var(--white);border:1px solid #9fb8d4;display:flex;align-items:center;padding:0 16px;font-size:10.5px;font-weight:600;letter-spacing:.04em;color:#143764;white-space:nowrap}
.faq-item::before{content:"";width:5px;height:5px;border-radius:50%;background:var(--blue);margin-right:9px}
.faq-item .chev{margin-left:auto}
.faq-item.open{height:70px;background:var(--blue);color:var(--white);border-color:var(--blue);flex-direction:column;align-items:flex-start;justify-content:center;padding-left:30px}
.faq-item.open::before{position:absolute;left:16px;top:21px;background:var(--white)}
.faq-item.open p{font-size:9px;font-weight:400;letter-spacing:0;line-height:1.55;margin-top:5px}
.faq-item.open .chev{position:absolute;right:16px;top:12px}

/* cta */
.cta-wrap{top:3437px;height:420px;background:var(--navy)}
.cta{position:absolute;left:118px;top:66px;width:955px;height:310px;background:linear-gradient(135deg,#2a86d4 0%,#1b6fc0 50%,#175fae 100%)}
.cta .heli{position:absolute;left:60px;top:30px;width:380px;height:250px;background:radial-gradient(ellipse at 50% 50%,#0f2d55 0%,rgba(23,74,140,.6) 35%,rgba(27,111,192,0) 70%)}
.cta h2{position:absolute;left:519px;top:97px;font-family:"Michroma",sans-serif;font-size:21px;font-weight:400;white-space:nowrap}
.cta p{position:absolute;left:519px;top:138px;width:340px;font-size:10px;line-height:1.7;color:#e3eefa}

/* footer */
.footer{position:absolute;left:0;top:3838px;width:1200px;height:370px;background:var(--navy-deep);overflow:hidden}
.footer h4{position:absolute;top:26px;font-size:11px;font-weight:600;letter-spacing:.07em;white-space:nowrap}
.footer .col{position:absolute;top:54px;font-size:9px;line-height:2.35;color:#b8c6da}
.footer .contact{position:absolute;font-size:9px;color:#b8c6da;line-height:1.5;display:flex;gap:10px;align-items:flex-start}
.footer .contact .ic{width:20px;height:20px;border-radius:50%;border:1px solid #8ea3c1;flex:none;display:flex;align-items:center;justify-content:center}
.divider{position:absolute;width:1px;background:var(--line)}
.social{position:absolute;top:4074px;width:20px;height:20px;border-radius:50%;border:1px solid #8ea3c1}
</style>
</head>
<body>

<section class="hero">
  <div class="hero-photo" role="img" aria-label="Pilot and passenger wearing headsets inside a helicopter cockpit"></div>
  <div class="hero-shade"></div>
  <svg class="abs" style="left:0;top:120px" width="480" height="260" viewBox="0 0 480 260"><polygon points="0,0 380,0 260,240 0,240" fill="#0e2a52" opacity=".45"/></svg>
  <h1>SEE FLORIDA<br>FROM THE SKY</h1>
  <p class="lede">Premium helicopter tours over Tampa &amp; Sarasota.</p>
  <div class="badge" style="left:121px;width:116px"><span class="circ"></span><span><small>Pindle Rating</small>5.0 <span class="stars">★★★★★</span></span></div>
  <div class="badge" style="left:243px;width:146px"><span class="circ" style="background:#dde6f1"></span>FAA-Certified Pilots</div>
</section>

<header class="site-header">
  <div class="brand"><span class="dot"></span><span>SkyROAMER<small>.COM</small></span></div>
  <nav class="nav">
    <a style="left:302px">TOURS ⌄</a>
    <a style="left:369px">GIFT CARDS</a>
    <a style="left:464px">WHAT TO EXPECT</a>
    <a style="left:585px">REVIEWS</a>
    <a style="left:661px">OUR PILOTS</a>
    <a style="left:754px">FAQ</a>
  </nav>
  <span class="user-icon"></span>
  <div class="btn" style="left:849px;top:44px;width:128px;height:31px"><span class="label">CONTACT US</span><span class="flag"><svg width="10" height="10" viewBox="0 0 10 10"><path d="M1 1v8M1 1h7v4H1" fill="none" stroke="#fff" stroke-width="1.2"/></svg></span></div>
  <div class="weather"><svg width="14" height="10" viewBox="0 0 14 10"><path d="M3 9h8a2.5 2.5 0 0 0 0-5 3.5 3.5 0 0 0-6.8 1A2 2 0 0 0 3 9z" fill="none" stroke="#fff"/></svg> <b>12°</b><br>Hourly Weather</div>
</header>

<div class="booking">
  <h2>PLAN A FLIGHT</h2>
  <span class="trip" style="left:163px"><i class="on"></i>One Way</span>
  <span class="trip" style="left:250px"><i></i>Round Trip</span>
  <span class="trip" style="left:348px"><i></i>Multi Trip</span>
  <div class="field" style="left:14px;width:162px">Location <span>⌄</span></div>
  <div class="field" style="left:184px;width:162px">Tour Type <span>⌄</span></div>
  <div class="field" style="left:353px;width:162px">Date &amp; Time <span>▦</span></div>
  <div class="field" style="left:522px;width:118px">⊖ &nbsp;1&nbsp; ⊕ <span>⚲</span></div>
  <div class="field" style="left:646px;width:163px">Contact &amp; Payment</div>
  <div class="btn" style="left:815px;top:52px;width:127px;height:33px"><span class="label">BOOK NOW</span><span class="flag">⚑</span></div>
</div>

<section class="reviews frame-lines">
  <h2 class="section-title" style="top:44px">WHAT CUSTOMERS ARE SAYING</h2>
  <article class="review faded" style="left:-128px"><p style="margin-top:72px">a first timer! My husband booked it and tour guide and our schedule work with.</p><span class="stars">★</span></article>
  <article class="review" style="left:121px">
    <div class="who"><span class="avatar" style="background:#1f8f7a"></span><div><h3>MARLA QUINTERO</h3><span class="when">2 weeks ago</span></div></div>
    <p>Such a great experience! My husband booked us the romantic flight as a suprise it was absolutely adorable. Definitely need to have a good tour guide and I liked ours.</p>
    <span class="stars">★★★★★</span><span class="src"></span>
  </article>
  <article class="review" style="left:364px">
    <div class="who"><span class="avatar" style="background:#8a6a4e"></span><div><h3>ROSALYN ASHBY<br>VENN</h3><span class="when">2 weeks ago</span></div></div>
    <p style="margin-top:14px">We had an incredible experience with SkyROAMER! From the moment we arrived, everything felt smooth, professional, and well organized. Our pilot was truly amazing - very friendly, knowledgeable, and took his time...</p>
    <span class="stars">★★★★★</span><span class="src"></span>
  </article>
  <article class="review" style="left:607px">
    <div class="who"><span class="avatar" style="background:#6b3a2e"></span><div><h3>TOMAS FERRIN</h3><span class="when">2 weeks ago</span></div></div>
    <p>This was an Early Christmas gift for my 9yr old special needs son. Everything exceeded my expectations and Corwin our pilot did an amazing job. He was super friendly and made sure my son was having a great time.</p>
    <span class="stars">★★★★★</span><span class="src"></span>
  </article>
  <article class="review" style="left:851px">
    <div class="who"><span class="avatar" style="background:#c9a58a"></span><div><h3>CELIA M</h3><span class="when">1 week ago</span></div></div>
    <p>Great experience for a first timer! Corwin was a great pilot and tour guide. Accommodated our schedule changes and easy to work with. Highly recommend!</p>
    <span class="stars">★★★★★</span><span class="src"></span>
  </article>
  <article class="review faded" style="left:1094px">
    <div class="who"><span class="avatar" style="background:#3a4f8a"></span><div><h3>CELIA</h3><span class="when">1 week ago</span></div></div>
    <p>Great experience Corwin was a great guide. Accommodated changes and easy recommend</p>
    <span class="stars">★★★★★</span>
  </article>
</section>

<section class="featured">
  <div class="abs" role="img" aria-label="Helicopter flying over the sea at sunset" style="left:300px;top:260px;width:600px;height:319px;background:radial-gradient(ellipse at 50% 75%,rgba(120,110,100,.35) 0%,rgba(205,183,159,0) 60%)"></div>
  <h2 class="section-title" style="top:62px">FEATURED EXPERIENCES</h2>
  <svg class="abs" style="left:0;top:0" width="1200" height="200">
    <line x1="139" y1="112" x2="1045" y2="112" stroke="#8d96a3" stroke-dasharray="2 3"/>
    <g fill="#1c73c8" stroke="#1c73c8">
      <circle cx="230" cy="157" r="4"/><line x1="230" y1="112" x2="230" y2="174"/>
      <circle cx="475" cy="157" r="4"/><line x1="475" y1="112" x2="475" y2="174"/>
      <circle cx="720" cy="157" r="4"/><line x1="720" y1="112" x2="720" y2="174"/>
      <circle cx="965" cy="157" r="4"/><line x1="965" y1="112" x2="965" y2="174"/>
    </g>
  </svg>
  <div class="feature" style="left:120px;top:171px"><span class="num">01</span><div class="pic" role="img" aria-label="Helicopter on a landing pad at dusk" style="background:radial-gradient(circle at 50% 40%,#4d5d6a,#1f2a35 70%,#c2571e 100%)"></div><h3>SEARCH &amp; QUOTE</h3><p>Curabitur faucibus quam ex, vel luctus tellus laoreet sit amet. Cras consequat vulputate mauris, sit amet pretium nisl fringilla ut.</p></div>
  <div class="feature" style="left:365px;top:171px"><span class="num">02</span><div class="pic" role="img" aria-label="Helicopter silhouetted against a golden sunset" style="background:radial-gradient(circle at 50% 50%,#f4c88a,#d78a45 70%,#b0672f)"></div><h3>SUNSET FLIGHTS</h3><p>Curabitur faucibus quam ex, vel luctus tellus laoreet sit amet. Cras consequat vulputate mauris, sit amet pretium nisl fringilla ut.</p></div>
  <div class="feature" style="left:610px;top:171px"><span class="num">03</span><div class="pic" role="img" aria-label="Couple celebrating beside a helicopter" style="background:radial-gradient(circle at 50% 50%,#d8d4cf,#8b8f98 70%,#4d5562)"></div><h3>ROMANTIC PACKAGES</h3><p>Curabitur faucibus quam ex, vel luctus tellus laoreet sit amet. Cras consequat vulputate mauris, sit amet pretium nisl fringilla ut.</p></div>
  <div class="feature" style="left:855px;top:171px"><span class="num">04</span><div class="pic" role="img" aria-label="Champagne toast aboard a helicopter" style="background:radial-gradient(circle at 50% 50%,#c08a4c,#5a4a6a 70%,#2a2f55)"></div><h3>CHAMPAGNE ADD-ONS</h3><p>Curabitur faucibus quam ex, vel luctus tellus laoreet sit amet. Cras consequat vulputate mauris, sit amet pretium nisl fringilla ut.</p></div>
</section>

<section class="gifts frame-lines">
  <span class="watermark" style="left:113px;top:240px">SKYROAMER</span>
  <h2 class="section-title" style="top:66px">GIVE AN EXPERIENCE THEY’LL NEVER FORGET</h2>
  <div class="gift" role="img" aria-label="Gift card with ribbon for birthdays" style="left:118px;background:linear-gradient(135deg,#1a5c9c,#2f7fc4 55%,#164d88)"><span class="corner">SR</span>Birthdays</div>
  <div class="gift" role="img" aria-label="Gift card with ribbon for anniversaries" style="left:359px;background:linear-gradient(135deg,#8e2a12,#c2461c 55%,#7a2410)"><span class="corner">SR</span>Anniversaries</div>
  <div class="gift" role="img" aria-label="Gift card with ribbon for proposals" style="left:601px;background:linear-gradient(135deg,#1a7a84,#2ea1a8 55%,#176670)"><span class="corner">SR</span>Proposals</div>
  <div class="gift" role="img" aria-label="Gift card with ribbon for gender reveals" style="left:843px;background:linear-gradient(135deg,#3a4bc2,#5d54d8 55%,#6b3dc0)"><span class="corner">SR</span>Gender Reveals</div>
  <div class="btn" style="left:516px;top:281px;width:160px;height:33px"><span class="label">BUY GIFT CARDS</span><span class="flag">⚑</span></div>
</section>

<section class="pilots">
  <div class="photo" role="img" aria-label="Pilot in sunglasses standing on an airfield beside a helicopter"></div>
  <h2>MEET THE PILOTS</h2>
  <p>SkyROAMER offers some of the most exciting Florida helicopter tours, empowering you to design your own custom aerial adventure across three iconic cities, with popular helicopter tours in Tampa and Sarasota. Whether you prefer a smooth, air-conditioned ride or crave the thrill of a doors-off helicopter tour, we deliver breathtaking views and unforgettable moments from takeoff to landing.</p>
  <div class="btn" style="left:122px;top:315px;width:152px;height:33px"><span class="label">LEARN MORE</span><span class="flag">⚑</span></div>
</section>

<section class="compare frame-lines">
  <svg class="abs" style="left:113px;top:60px" width="260" height="320" viewBox="0 0 260 320"><path d="M0 0h240v60H60v260H0z" fill="#102a50" opacity=".6"/></svg>
  <span class="watermark" style="left:300px;top:340px">SKYROAMER</span>
  <h2 class="section-title" style="top:96px;left:100px">COMPARE OUR HELICOPTER TOURS</h2>
  <table class="tour-table">
    <thead><tr><th style="width:165px">TOUR</th><th style="width:108px">DURATION</th><th style="width:212px">ROUTE HIGHLIGHTS</th><th style="width:153px">DOORS-OFF</th><th>DOORS-OFF</th></tr></thead>
    <tbody>
      <tr><td>Tampa Scenic Tour</td><td>15 min</td><td>Downtown Tampa, Bayshore,<br>waterfront skyline</td><td>Optional</td><td>From $130</td></tr>
      <tr><td>Tampa Sunset Flight</td><td>20 min</td><td>Tampa Bay at golden hour</td><td>Optional</td><td>From $280</td></tr>
      <tr><td>Sarasota Scenic Tour</td><td>15 min</td><td>Beaches, coastline, Gulf views</td><td>Optional</td><td>From $170</td></tr>
      <tr><td>Sarasota Sunset Flight</td><td>20 min</td><td>Gulf Coast sunset views</td><td>Optional</td><td>From $280</td></tr>
      <tr><td>Romantic Flight</td><td>20–30 min</td><td>Custom scenic route</td><td>Optional</td><td>From $130</td></tr>
      <tr><td>Gender Reveal Flight</td><td>Custom</td><td>Celebration reveal route</td><td>No</td><td>From $280</td></tr>
    </tbody>
  </table>
</section>

<section class="faq">
  <div class="abs" role="img" aria-label="Aerial view of a waterfront city skyline and marina" style="left:0;top:160px;width:1200px;height:329px;background:linear-gradient(180deg,rgba(230,236,242,0) 0%,rgba(150,170,185,.5) 50%,rgba(90,115,130,.7) 100%)"></div>
  <h2 class="section-title" style="top:60px">FREQUENTLY ASKED QUESTIONS</h2>
  <div class="faq-item open" style="top:111px"><span>IS IT SAFE TO FLY WITH SKYROAMER?</span><p>Yes. Safety is our top priority. All SkyROAMER flights are operated by<br>FAA-certified pilots using professionally maintained aircraft. Every guest</p><span class="chev">⌃</span></div>
  <div class="faq-item" style="top:191px">WHAT HAPPENS IF THE WEATHER IS BAD?<span class="chev">⌄</span></div>
  <div class="faq-item" style="top:232px">WHERE DO THE TOURS DEPART FROM?<span class="chev">⌄</span></div>
  <div class="faq-item" style="top:272px">HOW EARLY SHOULD I ARRIVE FOR MY FLIGHT?<span class="chev">⌄</span></div>
  <div class="faq-item" style="top:315px">WHAT SHOULD I WEAR?<span class="chev">⌄</span></div>
  <div class="faq-item" style="top:356px">CAN CHILDREN FLY?<span class="chev">⌄</span></div>
  <div class="faq-item" style="top:397px">HOW MANY PASSENGERS FIT IN THE HELICOPTER?<span class="chev">⌄</span></div>
</section>

<section class="cta-wrap frame-lines">
  <div class="cta">
    <div class="heli" role="img" aria-label="Helicopter flying through a blue sky"></div>
    <h2>READY FOR TAKEOFF?</h2>
    <p>Experience Florida from a whole new perspective — unforgettable helicopter tours over Tampa &amp; Sarasota.</p>
    <div class="btn" style="left:519px;top:179px;width:176px;height:33px;background:var(--white);color:#143764"><span class="label">BOOK YOUR FLIGHT</span><span class="flag" style="border-color:#c5d3e4;color:var(--blue)">⚑</span></div>
    <div class="btn" style="left:701px;top:179px;width:162px;height:33px;background:#5f9fdc"><span class="label">BUY GIFT CARDS</span><span class="flag">⚑</span></div>
  </div>
</section>

<footer class="footer">
  <span class="watermark" style="left:250px;top:250px;font-size:110px">SKYROAMER</span>
  <div class="brand" style="left:114px;top:28px"><span class="dot"></span><span>SkyROAMER<small>.COM</small></span></div>
  <p class="abs" style="left:114px;top:96px;width:215px;font-size:9px;line-height:1.75;color:#b8c6da">SkyROAMER offers some of the most exciting Florida helicopter tours, empowering you to design your own custom aerial adventure across three iconic cities, with popular helicopter tours in Tampa and Sarasota.</p>
  <span class="divider" style="left:344px;top:20px;height:190px"></span>
  <span class="divider" style="left:500px;top:20px;height:190px"></span>
  <span class="divider" style="left:694px;top:20px;height:190px"></span>
  <span class="divider" style="left:880px;top:20px;height:190px"></span>
  <h4 style="left:379px">COMPANY</h4>
  <div class="col" style="left:379px">Tours<br>Gift Cards<br>What to Expect<br>Reviews<br>Our Pilots<br>FAQ<br>Contact</div>
  <h4 style="left:522px">CONTACT US</h4>
  <div class="contact" style="left:522px;top:56px"><span class="ic"><svg width="8" height="10" viewBox="0 0 8 10"><path d="M4 9.5S1 6 1 4a3 3 0 0 1 6 0c0 2-3 5.5-3 5.5z" fill="none" stroke="#b8c6da"/></svg></span><span>420 Harbor Kite Ln, Tampa, FL,<br>United States, Florida</span></div>
  <div class="contact" style="left:522px;top:109px;align-items:center"><span class="ic"><svg width="9" height="9" viewBox="0 0 9 9"><path d="M1.5 1h2l1 2-1 1a5 5 0 0 0 1.5 1.5l1-1 2 1v2A6.5 6.5 0 0 1 1.5 1z" fill="none" stroke="#b8c6da" stroke-width=".8"/></svg></span><span>+1 800-555-0147</span></div>
  <div class="contact" style="left:522px;top:160px;align-items:center"><span class="ic"><svg width="10" height="8" viewBox="0 0 10 8"><rect x=".5" y=".5" width="9" height="7" fill="none" stroke="#b8c6da"/><path d="M.5 .5l4.5 4 4.5-4" fill="none" stroke="#b8c6da"/></svg></span><span>info@skyroamer-example.com</span></div>
  <h4 style="left:722px">HOTLINE HOURS</h4>
  <div class="col" style="left:722px;line-height:2.05">Mon 09:00 am – 05:30 pm<br>Tue 09:00 am – 05:30 pm<br>Wed 09:00 am – 05:30 pm<br>Thu 09:00 am – 05:30 pm<br>Fri 09:00 am – 05:30 pm<br>Sat 09:00 am – 05:30 pm<br>Sun 10:00 am – 03:00 pm</div>
  <h4 style="left:903px">SUBSCRIBE NEWSLETTER</h4>
  <div class="abs" style="left:904px;top:52px;width:158px;height:33px;border:1px solid #3a5478;display:flex;align-items:center;padding-left:10px"><svg width="11" height="8" viewBox="0 0 11 8"><rect x=".5" y=".5" width="10" height="7" fill="none" stroke="#8ea3c1"/><path d="M.5 .5l5 4 5-4" fill="none" stroke="#8ea3c1"/></svg></div>
  <div class="btn" style="left:904px;top:96px;width:126px;height:33px;background:var(--white);color:#143764"><span class="label">SUBSCRIBE</span><span class="flag" style="border-color:#c5d3e4;color:var(--blue)">⚑</span></div>
  <span class="abs" style="left:113px;top:212px;width:965px;height:1px;background:var(--line)"></span>
  <p class="abs" style="left:600px;top:232px;width:478px;text-align:right;font-size:8px;letter-spacing:.06em;color:#b8c6da">COPYRIGHT © 2026 SKYROAMER. ALL RIGHTS RESERVED</p>
</footer>
<span class="social" style="left:114px"></span>
<span class="social" style="left:146px"></span>
<span class="social" style="left:178px"></span>

</body>
</html>
```